Lernoptic.com Business Card Design Project

We need a new business card design for our new online company that delivers online education. It initially focused on SEO training but will soon offer more. The design should be fresh and trendy and take into account the colors and website design attached.
Industry/Entity Type
Training

```html
<!DOCTYPE html>
<html lang="en">
<head>
<meta charset="utf-8">
<title>Lernoptic.com Business Card</title>
<link rel="stylesheet" href="https://fonts.googleapis.com/css2?family=Cabin+Condensed:wght@400;500&family=Tinos&display=swap">
<style>
  :root {
    --brand-green: #007f45;
    --brand-grey: #6d6e71;
    --ink: #2a2a2a;
    --paper: #ffffff;
    --pointer-light: #d9d9da;
    --pointer-dark: #8a8b8e;
  }
  * { margin: 0; padding: 0; box-sizing: border-box; }
  html, body {
    width: 1200px;
    height: 704px;
    overflow: hidden;
    background: var(--paper);
  }
  .card {
    position: relative;
    width: 1200px;
    height: 704px;
    background: var(--paper);
    overflow: hidden;
  }
  .brand-mark {
    position: absolute;
    left: 50px;
    top: 140px;
    width: 124px;
    height: 124px;
    background: var(--brand-green);
  }
  .brand-name {
    position: absolute;
    left: 200px;
    top: 125px;
    font-family: "Cabin Condensed", sans-serif;
    font-weight: 400;
    font-size: 135px;
    line-height: 1;
    letter-spacing: 2px;
    color: var(--brand-grey);
    white-space: nowrap;
  }
  .web-address {
    position: absolute;
    left: 180px;
    top: 255px;
    font-family: "Tinos", serif;
    font-size: 59px;
    line-height: 1;
    color: var(--ink);
    white-space: nowrap;
  }
  .pointer-artwork {
    position: absolute;
    left: 856px;
    top: 143px;
    width: 190px;
    height: 318px;
    background: linear-gradient(160deg, var(--pointer-light), var(--pointer-dark));
  }
  .tagline-band {
    position: absolute;
    left: 0;
    bottom: 0;
    width: 1200px;
    height: 91px;
    background: var(--brand-green);
  }
  .tagline-word {
    position: absolute;
    top: 50%;
    transform: translate(-50%, -50%);
    font-family: "Cabin Condensed", sans-serif;
    font-weight: 500;
    font-size: 44px;
    line-height: 1;
    color: var(--paper);
    white-space: nowrap;
  }
  .tagline-word--strategic { left: 267px; }
  .tagline-word--internet { left: 579px; }
  .tagline-word--mastery { left: 886px; }
</style>
</head>
<body>
  <main class="card">
    <div class="brand-mark" aria-hidden="true"></div>
    <div class="brand-name">lernoptic</div>
    <div class="web-address">www.yourURL.co.uk</div>

    <div class="pointer-artwork" role="img" aria-label="Illustration of a large pixel-style grey mouse pointer"></div>

    <footer class="tagline-band">
      <span class="tagline-word tagline-word--strategic">Strategic</span>
      <span class="tagline-word tagline-word--internet">Internet</span>
      <span class="tagline-word tagline-word--mastery">Mastery</span>
    </footer>
  </main>
</body>
</html>
```